Business Card for Beach theme sports bar called TAVRU

I need a business card designed for our employees, front and back. This will be used by the employees of two business locations to hand out to customers. I've attached the previous business cards we used at one time for a Benwicks (it is now Tavru). Looking for a fresh new card that is elegant but has character.

Target Market(s)

30-60, middle class

Contact Information for Business Card

We are a beach bar and sports bar. I am looking for an elegant business card with the front to have the TAVRU logo. Then on the back I need it to allow a space for employees to write their names and for them to write in their schedule. I have attached our old cards with our old name Benwicks so you can pull everything we need on the cards. one thing is missing is we have another location at 2815 N Willow Crest Rd with a number of 702-418-9351. Since we will use it for both locations it should allow the employee to circle or check mark the bar which they work at.

Font styles to use
Sans Serif

Requirements
Must have
• We are looking for some fresh ideas for the business card. Something that will really stick out to customers when the staff hands them out. Creativity will be looked at positively, but we still want it to look upscale and fun.

```html
<!DOCTYPE html>
<html lang="en">
<head>
<meta charset="utf-8">
<title>Tavru Business Cards</title>
<link href="https://fonts.googleapis.com/css2?family=Barlow:wght@300;400;600;700&family=Barlow+Semi+Condensed:wght@300;400&family=Allura&display=swap" rel="stylesheet">
<style>
  :root {
    --sun: #f5c660;
    --sun-soft: #fbe7b8;
    --mint: #bfe3d8;
    --mint-soft: #def1eb;
    --ink: #111111;
    --paper: #ffffff;
    --line-grey: #b9b9b9;
  }
  * { box-sizing: border-box; margin: 0; padding: 0; }
  html, body { width: 1200px; height: 849px; overflow: hidden; background: var(--paper); }
  .sheet { position: relative; width: 1200px; height: 849px; font-family: "Barlow", sans-serif; color: var(--ink); }

  .sheet-title {
    position: absolute; top: 60px; left: 0; width: 100%;
    text-align: center; font-family: "Barlow Semi Condensed", sans-serif;
    font-weight: 300; font-size: 25px; line-height: 31px; letter-spacing: 0.5px;
  }

  .card { position: absolute; width: 343px; height: 222px; overflow: hidden; }
  .card-front { top: 156px; display: flex; align-items: center; justify-content: center; gap: 12px; }
  .card-front.sun { background: var(--sun); }
  .card-front.mint { background: var(--mint); }
  .card-front.night { background: var(--ink); color: var(--paper); }
  .brand-name { font-family: "Barlow", sans-serif; font-weight: 700; font-size: 46px; letter-spacing: 3px; }
  .brand-dot { width: 14px; height: 14px; border-radius: 50%; background: currentColor; }

  .card-back { top: 411px; background: var(--paper); border: 1.5px solid var(--ink); }
  .col-1 { left: 69px; }
  .col-2 { left: 438px; }
  .col-3 { left: 811px; }

  .role-band {
    position: absolute; left: 14px; top: 17px; width: 309px; height: 45px;
    border-radius: 22px; display: flex; align-items: center; padding-left: 21px;
  }
  .sun .role-band { background: var(--sun); }
  .mint .role-band { background: var(--mint); }
  .role-label { font-weight: 700; font-size: 15px; letter-spacing: 0.2px; }
  .name-field {
    position: absolute; left: 129px; top: 9px; width: 174px; height: 27px; background: var(--paper);
    font-family: "Allura", cursive; font-size: 26px; line-height: 30px; padding-left: 22px;
  }

  .role-plain { position: absolute; left: 49px; top: 23px; display: flex; align-items: flex-end; }
  .role-plain .name-line {
    font-family: "Allura", cursive; font-size: 26px; line-height: 24px;
    margin-left: 10px; width: 153px; border-bottom: 1px solid #555; padding-left: 20px;
  }

  .schedule { position: absolute; left: 58px; display: grid; grid-template-columns: repeat(7, 26px); column-gap: 7.6px; }
  .sun .schedule, .mint .schedule { top: 80px; }
  .night-back .schedule { top: 68px; }
  .day { text-align: center; font-size: 13px; line-height: 16px; margin-bottom: 4px; font-weight: 400; }
  .box { width: 26px; height: 23px; border: 1.5px solid var(--ink); position: relative; }
  .sun .box { border-color: var(--sun); }
  .mint .box { border-color: var(--mint); }
  .box.marked svg { position: absolute; inset: 2px; }

  .locations { position: absolute; left: 0; width: 100%; display: flex; justify-content: space-around; padding: 0 36px; }
  .sun .locations, .mint .locations { top: 136px; }
  .night-back .locations { top: 132px; }
  .location { width: 120px; text-align: center; font-size: 8px; line-height: 10.5px; font-weight: 600; }
  .marker { position: relative; width: 22px; height: 22px; margin: 0 auto 6px; border-radius: 50%; border: 1.2px solid var(--line-grey); }
  .sun .marker { border-color: var(--sun); }
  .mint .marker { border-color: var(--mint); }
  .marker svg { position: absolute; inset: -2px; }

  .option-label {
    position: absolute; top: 670px; width: 343px; text-align: center;
    font-family: "Barlow Semi Condensed", sans-serif; font-weight: 400; font-size: 26px;
  }
</style>
</head>
<body>
<main class="sheet">
  <h1 class="sheet-title">Business Cards<br>3,4 x 2 in</h1>

  <section class="card card-front sun col-1"><span class="brand-name">TAVRU</span><span class="brand-dot"></span></section>
  <section class="card card-front mint col-2"><span class="brand-name">TAVRU</span><span class="brand-dot"></span></section>
  <section class="card card-front night col-3"><span class="brand-name">TAVRU</span><span class="brand-dot"></span></section>

  <!-- Back, sun -->
  <section class="card card-back sun col-1">
    <div class="role-band"><span class="role-label">BARTENDER</span><span class="name-field">My Nameis</span></div>
    <div class="schedule">
      <span class="day">M</span><span class="day">T</span><span class="day">W</span><span class="day">Th</span><span class="day">F</span><span class="day">Sa</span><span class="day">Su</span>
      <span class="box marked"><svg viewBox="0 0 20 17" width="20" height="17"><path d="M4 15 L16 2 M5 3 L15 15" stroke="#111" stroke-width="1" fill="none"/></svg></span><span class="box"></span><span class="box"></span><span class="box"></span><span class="box"></span><span class="box"></span><span class="box"></span>
    </div>
    <div class="locations">
      <div class="location"><div class="marker"></div>6140 W Harbor Mist Rd<br>Las Vegas, NV 89146<br>702-555-0142<br>cs@tavrubar.com</div>
      <div class="location"><div class="marker"><svg viewBox="0 0 26 26" width="26" height="26"><path d="M7 22 L19 4 M8 5 L18 21" stroke="#111" stroke-width="1" fill="none"/></svg></div>2815 N Willow Crest Rd<br>Las Vegas, NV 89147<br>702-418-9351<br>cs@tavrubar.com</div>
    </div>
  </section>

  <!-- Back, mint -->
  <section class="card card-back mint col-2">
    <div class="role-band"><span class="role-label">BARTENDER</span><span class="name-field">My Nameis</span></div>
    <div class="schedule">
      <span class="day">M</span><span class="day">T</span><span class="day">W</span><span class="day">Th</span><span class="day">F</span><span class="day">Sa</span><span class="day">Su</span>
      <span class="box marked"><svg viewBox="0 0 20 17" width="20" height="17"><path d="M4 15 L16 2 M5 3 L15 15" stroke="#111" stroke-width="1" fill="none"/></svg></span><span class="box"></span><span class="box"></span><span class="box"></span><span class="box"></span><span class="box"></span><span class="box"></span>
    </div>
    <div class="locations">
      <div class="location"><div class="marker"></div>6140 W Harbor Mist Rd<br>Las Vegas, NV 89146<br>702-555-0142<br>cs@tavrubar.com</div>
      <div class="location"><div class="marker"><svg viewBox="0 0 26 26" width="26" height="26"><path d="M7 22 L19 4 M8 5 L18 21" stroke="#111" stroke-width="1" fill="none"/></svg></div>2815 N Willow Crest Rd<br>Las Vegas, NV 89147<br>702-418-9351<br>cs@tavrubar.com</div>
    </div>
  </section>

  <!-- Back, monochrome -->
  <section class="card card-back night-back col-3">
    <div class="role-plain"><span class="role-label">BARTENDER</span><span class="name-line">My Nameis</span></div>
    <div class="schedule">
      <span class="day">M</span><span class="day">T</span><span class="day">W</span><span class="day">Th</span><span class="day">F</span><span class="day">Sa</span><span class="day">Su</span>
      <span class="box marked"><svg viewBox="0 0 20 17" width="20" height="17"><path d="M4 15 L16 2 M5 3 L15 15" stroke="#111" stroke-width="1" fill="none"/></svg></span><span class="box"></span><span class="box"></span><span class="box"></span><span class="box"></span><span class="box"></span><span class="box"></span>
    </div>
    <div class="locations">
      <div class="location"><div class="marker"></div>6140 W Harbor Mist Rd<br>Las Vegas, NV 89146<br>702-555-0142<br>cs@tavrubar.com</div>
      <div class="location"><div class="marker"><svg viewBox="0 0 26 26" width="26" height="26"><path d="M7 22 L19 4 M8 5 L18 21" stroke="#111" stroke-width="1" fill="none"/></svg></div>2815 N Willow Crest Rd<br>Las Vegas, NV 89147<br>702-418-9351<br>cs@tavrubar.com</div>
    </div>
  </section>

  <p class="option-label col-1">Option 1</p>
  <p class="option-label col-2">Option 2</p>
  <p class="option-label col-3">Option 3</p>
</main>
</body>
</html>
```